Design a website for a new innovative shipping service

Parcivo.com is a new business concept that makes it easy and inexpensive for private individuals to ship packages to friends and families abroad. It is basically a website where customers can create and print shipping labels that they can put on their package and then drop off the package at any postal office.

We need an initial site design for the launch of the concept. The site is fairly simple – see the design brief and wireframes - both uploadet

We expect design of the entire label creation flow as well as basic content pages.

Target Market(s)

See design brief

Industry/Entity Type

Business

Number of Pages Required

5+ page

Requirements
Must have
• See design brief
Nice to have
• See design brief
Should not have
• See design brief

```html
<!DOCTYPE html>
<html lang="en">
<head>
<meta charset="utf-8">
<title>Parcivo – Enter Sender Information</title>
<link rel="stylesheet" href="https://fonts.googleapis.com/css2?family=Open+Sans:wght@400;600;700&display=swap">
<style>
  :root {
    --navy: #1f2d3d;
    --navy-deep: #17222f;
    --orange: #f58220;
    --orange-dark: #e06d0c;
    --white: #ffffff;
    --ink: #2a2a2a;
    --muted: #7a7f86;
    --field-border: #cfd4da;
  }
  * { box-sizing: border-box; margin: 0; padding: 0; }
  html, body { width: 882px; height: 1200px; overflow: hidden; }
  body { font-family: "Open Sans", Arial, sans-serif; color: var(--ink); background: var(--white); position: relative; }

  .hero {
    position: absolute; left: 0; top: 0; width: 882px; height: 250px;
    background: linear-gradient(90deg, #c7c3bd 0%, #a99b8c 30%, #8a7b6d 55%, #b9b2aa 80%, #d4d0cb 100%);
  }
  .hero-shade { position: absolute; inset: 0; background: linear-gradient(180deg, rgba(20,30,45,.15), rgba(20,30,45,.55)); }
  .brand { position: absolute; left: 30px; top: 20px; display: flex; align-items: center; gap: 8px; color: var(--white); font-weight: 700; font-size: 22px; }
  .brand-mark { width: 20px; height: 20px; background: var(--orange); }
  .lang { position: absolute; right: 70px; top: 22px; border: 1px solid rgba(255,255,255,.7); color: var(--white); font-size: 11px; padding: 2px 8px; }
  .hero-title { position: absolute; left: 0; right: 0; top: 100px; text-align: center; color: var(--white); font-size: 32px; font-weight: 700; letter-spacing: 1px; }
  .hero-sub { position: absolute; left: 0; right: 0; top: 146px; text-align: center; color: var(--orange); font-size: 13px; font-weight: 600; }

  .social { position: absolute; right: 0; top: 160px; width: 20px; z-index: 5; }
  .social span { display: block; width: 20px; height: 22px; margin-bottom: 2px; }
  .s1 { background: #3b5998; } .s2 { background: #1da1f2; } .s3 { background: #0e76a8; } .s4 { background: #dd4b39; } .s5 { background: #cb2027; }

  .form-band { position: absolute; left: 0; top: 250px; width: 882px; height: 440px; background: var(--navy); }
  .step-icon { position: absolute; left: 421px; top: -46px; width: 40px; height: 40px; border-radius: 50%; border: 2px solid var(--orange); background: var(--navy); display: flex; align-items: center; justify-content: center; }
  .sender-form { position: absolute; left: 194px; top: 12px; width: 496px; }
  .field { display: block; width: 100%; height: 34px; background: var(--white); border: 1px solid var(--field-border); border-radius: 2px; font-size: 11px; color: var(--muted); padding: 0 10px; line-height: 34px; margin-bottom: 14px; }
  .row { display: flex; gap: 12px; }
  .row .field { flex: 1; }
  .select { position: relative; }
  .select .caret { position: absolute; right: -1px; top: -1px; width: 30px; height: 34px; background: var(--orange); display: flex; align-items: center; justify-content: center; }
  .country { color: var(--white); font-size: 13px; font-weight: 700; margin: 0 0 12px; }
  .country em { color: var(--orange); font-style: normal; font-weight: 400; }
  .continue { display: block; margin: 22px auto 0; width: 156px; height: 36px; background: var(--orange); color: var(--white); border: none; border-radius: 3px; font: 600 14px "Open Sans", Arial, sans-serif; }
  .prev { text-align: center; color: var(--orange); font-size: 11px; margin-top: 10px; }
  .help { text-align: center; color: #8d97a3; font-size: 9px; margin-top: 12px; }

  .ship { position: absolute; left: 0; top: 690px; width: 882px; height: 383px; text-align: center; }
  .ship h2 { font-size: 32px; font-weight: 600; color: var(--ink); margin-top: 26px; }
  .ship p { width: 560px; margin: 14px auto 0; font-size: 11px; color: var(--muted); line-height: 1.6; }
  .ship h3 { color: var(--orange); font-size: 20px; font-weight: 700; margin-top: 8px; }
  .items { position: absolute; left: 130px; top: 185px; display: flex; gap: 38px; align-items: flex-end; }
  .item { border-radius: 6px; }
  .bag { width: 145px; height: 145px; background: linear-gradient(180deg, #f48b3c, #d8601a); }
  .statue { width: 110px; height: 150px; background: linear-gradient(180deg, #c9a26a, #8a6a3e); }
  .gift { width: 130px; height: 140px; background: linear-gradient(180deg, #f39a3a 0 30%, #3aa3d9 30% 100%); }
  .shoes { width: 160px; height: 90px; background: linear-gradient(180deg, #3a3d44, #b8382f); }

  .testimonials { position: absolute; left: 0; top: 1073px; width: 882px; height: 87px; background: var(--orange); }
  .t-label { position: absolute; left: 103px; top: 0; width: 177px; height: 87px; background: var(--orange-dark); color: var(--white); padding: 20px 16px; }
  .t-label strong { display: block; font-size: 14px; }
  .t-label small { font-size: 9px; }
  .avatar { position: absolute; left: 315px; top: 14px; width: 58px; height: 58px; border-radius: 50%; background: #e8d8c8; border: 3px solid var(--white); }
  .quote { position: absolute; left: 392px; top: 14px; width: 420px; color: var(--white); }
  .quote b { font-size: 10px; display: block; margin-bottom: 4px; }
  .quote span { font-size: 9px; line-height: 1.5; display: block; }

  .site-footer { position: absolute; left: 0; top: 1160px; width: 882px; height: 40px; background: var(--navy-deep); color: var(--white); font-size: 11px; }
  .footer-nav { position: absolute; left: 128px; top: 12px; display: flex; gap: 30px; }
  .footer-nav a:first-child { border-bottom: 2px solid var(--orange); }
  .footer-dot { position: absolute; left: 434px; top: 13px; width: 14px; height: 14px; border-radius: 50%; background: var(--orange); }
  .copyright { position: absolute; right: 130px; top: 13px; font-size: 9px; color: #9aa4ae; }
  a { color: inherit; text-decoration: none; }
</style>
</head>
<body>
  <header class="hero">
    <div class="hero-shade" role="img" aria-label="Photo of a smiling woman holding a parcel"></div>
    <div class="brand"><span class="brand-mark"></span>Parcivo</div>
    <div class="lang">EN</div>
    <h1 class="hero-title">ENTER SENDER INFORMATION</h1>
    <div class="hero-sub">01</div>
  </header>

  <nav class="social" aria-label="Social links">
    <span class="s1"></span><span class="s2"></span><span class="s3"></span><span class="s4"></span><span class="s5"></span>
  </nav>

  <section class="form-band">
    <div class="step-icon" aria-hidden="true">
      <svg width="16" height="16" viewBox="0 0 16 16"><path d="M8 2 V13 M3 8 L8 13 L13 8" fill="none" stroke="#f58220" stroke-width="2" stroke-linecap="round" stroke-linejoin="round"/></svg>
    </div>
    <form class="sender-form">
      <div class="field">Sender Name</div>
      <div class="field">Address line 1</div>
      <div class="field">Address line 2</div>
      <div class="row">
        <div class="field">Zip Code</div>
        <div class="field select">City<span class="caret"><svg width="10" height="6" viewBox="0 0 10 6"><path d="M0 0 L5 6 L10 0 Z" fill="#fff"/></svg></span></div>
      </div>
      <div class="country">Country / <em>Denmark</em></div>
      <div class="row">
        <div class="field">Phone no</div>
        <div class="field">Email ID</div>
      </div>
      <button type="button" class="continue">Continue &gt;</button>
      <div class="prev">Previous Step</div>
      <div class="help">Need help? Check out our FAQ</div>
    </form>
  </section>

  <section class="ship">
    <h2>What do you want to ship?</h2>
    <p>No matter who you are, an individual or a business, you should not be spending time and money on sending things to people that you care about. We are here to help you.</p>
    <h3>THAT CAN BE ANYTHING</h3>
    <div class="items">
      <div class="item bag" role="img" aria-label="Orange handbag"></div>
      <div class="item statue" role="img" aria-label="Small bronze statue"></div>
      <div class="item gift" role="img" aria-label="Blue gift box with orange ribbon"></div>
      <div class="item shoes" role="img" aria-label="Pair of sneakers"></div>
    </div>
  </section>

  <section class="testimonials">
    <div class="t-label"><strong>Testimonials</strong><small>What our customers say</small></div>
    <div class="avatar" role="img" aria-label="Customer portrait"></div>
    <div class="quote">
      <b>MARA LINDQVIST, CUSTOMER</b>
      <span>The Parcivo team has made our website the best in our industry. Some of our competitors even complimented us on it. Lots of thanks to the Parcivo team and the whole shipping flow.</span>
    </div>
  </section>

  <footer class="site-footer">
    <div class="footer-nav"><a href="#">About</a><a href="#">Terms</a><a href="#">Help</a></div>
    <span class="footer-dot"></span>
    <div class="copyright">Copyright ©2015 Parcivo</div>
  </footer>
</body>
</html>
```